Mental Health & Addiction Podcast Art

Project: Podcast Cover Art / Visual Identity
Podcast Name: The Mending Path
Focus: Recovery from substance use and mental health
Objectives
Create compelling podcast artwork that:
Reflects the themes of hope, healing, and personal growth
Establishes credibility and professionalism
Appeals to individuals seeking recovery resources and support
Maintains strong brand consistency with Larkspur Wellness
Brand Integration Requirements
Logo incorporation: Integrate an element from the Larkspur Wellness Logo—potentially an abstract or partial use of the sun motif
Flexibility: Open to creative interpretations (e.g., sun rays as background texture, sunrise gradient, partial sun as a design accent)
Mandatory: Must adhere to existing Larkspur Wellness brand guidelines (approved color palette, typography, and visual style)

Target Market(s)

United states, people with addiction and mental health disorders.

Industry/Entity Type

Wellness

Font styles to use
Other font styles liked:
• See Brand Guide

Requirements
Must have
• Match brand guide, in corporate elements of the Larkspur Wellness Logo icon

```html
<!DOCTYPE html>
<html lang="en">
<head>
<meta charset="utf-8">
<title>The Mending Path — Podcast Cover</title>
<link rel="stylesheet" href="https://fonts.googleapis.com/css2?family=Playfair+Display:wght@400;700;900&family=IBM+Plex+Sans:wght@300;600;700&display=swap">
<style>
  :root {
    --sky-top: #4b50b8;
    --sky-mid: #2a5fc6;
    --deep-teal: #0c3646;
    --night: #05111a;
    --sun-gold: #f2b134;
    --paper: #ffffff;
    --silver-light: #ffffff;
    --silver-dark: #b9bcc2;
    --rule: rgba(255,255,255,0.55);
    --portrait-hair: #2b1a13;
    --portrait-shirt: #1a2550;
  }
  html, body {
    margin: 0;
    padding: 0;
    width: 1200px;
    height: 1200px;
    overflow: hidden;
    background: var(--night);
  }
  .cover {
    position: relative;
    width: 1200px;
    height: 1200px;
    overflow: hidden;
    background: linear-gradient(180deg, var(--sky-top) 0%, var(--sky-mid) 42%, #1d4f9a 58%, var(--deep-teal) 72%, var(--night) 92%);
  }
  .portrait {
    position: absolute;
    left: 440px;
    top: 48px;
    width: 760px;
    height: 1152px;
    border-radius: 320px 300px 0 0;
    background: linear-gradient(165deg, var(--portrait-hair) 0%, #4a2c1e 38%, #2a2030 62%, var(--portrait-shirt) 100%);
  }
  .title-article {
    position: absolute;
    left: 64px;
    top: 40px;
    margin: 0;
    font-family: "Playfair Display", Georgia, serif;
    font-weight: 700;
    font-size: 84px;
    line-height: 1;
    color: var(--paper);
  }
  .title-vertical {
    position: absolute;
    left: 22px;
    top: 126px;
    width: 150px;
    margin: 0;
    writing-mode: vertical-rl;
    font-family: "Playfair Display", Georgia, serif;
    font-weight: 400;
    font-size: 150px;
    line-height: 150px;
    color: var(--sun-gold);
  }
  .pillars {
    position: absolute;
    left: 168px;
    top: 304px;
    width: 276px;
    margin: 0;
    padding: 0;
    list-style: none;
    font-family: "IBM Plex Sans", Arial, sans-serif;
    font-weight: 300;
    font-size: 23.5px;
    line-height: 24.5px;
    text-transform: uppercase;
    text-align: center;
    color: var(--paper);
  }
  .pillars li { padding: 0; }
  .pillars li + li {
    margin-top: 12px;
    padding-top: 14px;
    background: linear-gradient(var(--rule), var(--rule)) center top / 184px 1px no-repeat;
  }
  .title-main {
    position: absolute;
    left: 50px;
    top: 714px;
    width: 1100px;
    margin: 0;
    font-family: "Playfair Display", Georgia, serif;
    font-weight: 900;
    font-size: 392px;
    line-height: 1;
    letter-spacing: 22px;
    text-align: center;
    background: linear-gradient(180deg, var(--silver-light) 20%, #e4e5e8 55%, var(--silver-dark) 100%);
    -webkit-background-clip: text;
    background-clip: text;
    color: transparent;
  }
  .tagline {
    position: absolute;
    left: 0;
    top: 1094px;
    width: 1200px;
    margin: 0;
    font-family: "IBM Plex Sans", Arial, sans-serif;
    font-weight: 700;
    font-size: 33px;
    line-height: 37px;
    letter-spacing: 5.4px;
    text-transform: uppercase;
    text-align: center;
    color: var(--paper);
  }
  .tagline-line { display: block; padding-left: 20px; }
  .tagline-ruled {
    display: flex;
    align-items: center;
    justify-content: center;
    gap: 22px;
    padding-left: 20px;
  }
  .tagline-ruled::before,
  .tagline-ruled::after {
    content: "";
    width: 108px;
    height: 2px;
    background: var(--paper);
  }
  .brand-mark {
    position: absolute;
    left: 940px;
    top: 80px;
    width: 230px;
    display: flex;
    flex-direction: column;
    align-items: center;
    gap: 10px;
  }
  .brand-dot {
    width: 34px;
    height: 34px;
    border-radius: 50%;
    background: var(--sun-gold);
  }
  .brand-name {
    margin: 0;
    font-family: "IBM Plex Sans", Arial, sans-serif;
    font-weight: 600;
    font-size: 26px;
    line-height: 30px;
    letter-spacing: 4px;
    text-transform: uppercase;
    text-align: center;
    color: var(--paper);
  }
</style>
</head>
<body>
  <main class="cover">
    <div class="portrait" role="img" aria-label="Photo of a smiling young woman with long curly dark hair in a navy top, looking back over her shoulder"></div>

    <p class="title-article">the</p>
    <p class="title-vertical">mending</p>

    <ul class="pillars">
      <li>Reflects the themes of hope, healing, and personal growth</li>
      <li>Establishes credibility and professionalism</li>
      <li>Appeals to individuals seeking recovery resources and support</li>
      <li>Maintains strong brand consistency with Larkspur Wellness</li>
    </ul>

    <h1 class="title-main">PATH</h1>

    <p class="tagline">
      <span class="tagline-line">Recovery from substance use and</span>
      <span class="tagline-ruled">Mental health</span>
    </p>

    <div class="brand-mark">
      <span class="brand-dot"></span>
      <p class="brand-name">Larkspur<br>Wellness</p>
    </div>
  </main>
</body>
</html>
```